Large multi-office optometry business opening a Dry Eye Spa and needs sign.

Business name/sign info: Brindlecove Dry Eye Institute, (555) 316-4872
Backlit pole sign at office entrance on a very busy street
Sign dimensions: 53" tall x 136.5" wide
State of the art Dry Eye Spa for treatment of all forms of dry eye and ocular surface disease. Also, have aesthetics treatments (IPL, Low Level Light Treatment, etc.)

Target Market(s)

People who are suffering from: dryness, burning, foreign body sensation, itching, fluctuating vision, tired eyes, etc.

Industry/Entity Type

Optometry and aesthetics

Colors
0054AA
0677BA
7BADD7
CADEEF
E8F1F8

Requirements
Must have
• Business name, phone number, subliminal message of relief in a glance or short look.
Nice to have
• Cool, relief, soothing sense.
Should not have
• Too much information or too busy.

```html
<!DOCTYPE html>
<html lang="en">
<head>
<meta charset="utf-8">
<title>Brindlecove Dry Eye Institute – Entrance Sign</title>
<link rel="stylesheet" href="https://fonts.googleapis.com/css2?family=Montserrat:wght@400;500;800&family=Roboto+Condensed:wght@400&family=Poppins:wght@800&display=swap">
<style>
  :root {
    --sky-top: #d9f0fb;
    --sky-mid: #7fcdf2;
    --sky-bottom: #0a9de4;
    --ink: #0b0b0b;
    --white: #ffffff;
    --skin-light: #f0d6c6;
    --skin-mid: #d9ad95;
    --skin-shadow: #a97a66;
    --skin-cool: #9fb3c0;
    --brand-violet: #4a3d8f;
  }
  * { margin: 0; padding: 0; box-sizing: border-box; }
  html, body { width: 1200px; height: 505px; overflow: hidden; background: var(--white); }

  .sign {
    position: relative;
    width: 1200px;
    height: 505px;
    overflow: hidden;
    background: linear-gradient(180deg, var(--sky-top) 0%, var(--sky-mid) 48%, var(--sky-bottom) 100%);
    font-family: "Montserrat", sans-serif;
    color: var(--ink);
  }

  .hero-photo {
    position: absolute;
    top: 0; right: 0;
    width: 600px; height: 505px;
    background:
      radial-gradient(ellipse 120px 70px at 62% 38%, rgba(190,205,215,0.55) 0%, rgba(190,205,215,0) 100%),
      radial-gradient(ellipse 150px 80px at 28% 48%, rgba(170,190,205,0.5) 0%, rgba(170,190,205,0) 100%),
      radial-gradient(ellipse 220px 260px at 38% 80%, var(--skin-light) 0%, rgba(240,214,198,0) 100%),
      radial-gradient(ellipse 340px 140px at 70% 8%, rgba(150,105,85,0.55) 0%, rgba(150,105,85,0) 100%),
      linear-gradient(90deg, var(--skin-cool) 0%, var(--skin-mid) 30%, var(--skin-light) 60%, var(--skin-mid) 100%);
    -webkit-mask-image: linear-gradient(90deg, transparent 0%, #000 22%);
    mask-image: linear-gradient(90deg, transparent 0%, #000 22%);
  }

  .headline {
    position: absolute;
    left: 37px; top: 30px;
    font-weight: 800;
    font-size: 73px;
    letter-spacing: -0.5px;
    line-height: 1;
    white-space: nowrap;
  }

  .tagline {
    position: absolute;
    left: 39px; top: 114px;
    font-weight: 400;
    font-size: 29px;
    line-height: 33px;
    white-space: nowrap;
  }

  .feature {
    position: absolute;
    top: 222px;
    width: 158px;
    font-family: "Roboto Condensed", sans-serif;
  }
  .feature--what { left: 39px; }
  .feature--expect { left: 220px; }
  .feature--offer { left: 401px; }

  .feature__title {
    font-size: 15px;
    font-weight: 400;
    line-height: 18px;
    margin-bottom: 6px;
    white-space: nowrap;
  }
  .feature__photo {
    width: 158px; height: 108px;
    border: 2px solid var(--white);
  }
  .feature--what .feature__photo { background: linear-gradient(160deg, #f4f8fb, #d5e3ec); }
  .feature--expect .feature__photo { background: linear-gradient(120deg, #3c4550, #9fb4c6 60%, #d7dee4); }
  .feature--offer .feature__photo { background: linear-gradient(90deg, #e8eef3 0%, #c9d3da 45%, #d8ab8c 75%, #8a5a3a 100%); }

  .feature__text {
    margin-top: 7px;
    font-size: 13.5px;
    line-height: 15.5px;
    text-align: center;
    color: var(--white);
  }

  .contact-line {
    position: absolute;
    left: 39px; top: 463px;
    font-family: "Poppins", sans-serif;
    font-weight: 800;
    font-size: 25px;
    line-height: 1;
    white-space: nowrap;
  }

  .brand-mark {
    position: absolute;
    left: 972px; top: 440px;
    display: flex;
    align-items: center;
    gap: 10px;
  }
  .brand-mark__dot {
    width: 34px; height: 34px;
    border-radius: 50%;
    background: var(--brand-violet);
  }
  .brand-mark__name {
    font-family: "Montserrat", sans-serif;
    font-weight: 500;
    font-size: 20px;
    color: var(--brand-violet);
    white-space: nowrap;
  }
</style>
</head>
<body>
  <main class="sign">
    <div class="hero-photo" role="img" aria-label="Close-up photograph of a woman's face showing both clear, bright eyes"></div>

    <h1 class="headline">State of the art</h1>
    <p class="tagline">Dry Eye Spa for treatment of all forms<br>of dry eye and ocular surface disease</p>

    <section class="feature feature--what">
      <h2 class="feature__title">What is Dry Eye?</h2>
      <div class="feature__photo" role="img" aria-label="Photograph of an eye drop falling from a bottle"></div>
      <p class="feature__text">Dry Eye Disease is a complex condition that has many causes and creates many symptoms.</p>
    </section>

    <section class="feature feature--expect">
      <h2 class="feature__title">What to Expect</h2>
      <div class="feature__photo" role="img" aria-label="Photograph of an eye beside an examination lens"></div>
      <p class="feature__text">We treat the cause, not just the symptoms &amp; develop a treatment plan that is specialized for you!</p>
    </section>

    <section class="feature feature--offer">
      <h2 class="feature__title">Complimentary Evaluation</h2>
      <div class="feature__photo" role="img" aria-label="Photograph of a patient at a slit-lamp eye examination"></div>
      <p class="feature__text">For a limited time only, you can receive our $199 Dry Eye Evaluation for Free!</p>
    </section>

    <p class="contact-line">Brindlecove Dry Eye Institute, (555) 316-4872</p>

    <div class="brand-mark">
      <span class="brand-mark__dot"></span>
      <span class="brand-mark__name">Clearwell Eye Spa</span>
    </div>
  </main>
</body>
</html>
```